Buch-/eBook-Cover für Buch zum Thema Verkauf auf Verkando
Zielgruppe
E-Commerce Plattform für Verkando Händler
Aufgabenstellung
Das Buch soll eine umfassende Anleitung für den Verkauf auf Verkando abbilden. Als Buchcover war die Überlegung, dieses wie ein typisches Verkando Paket aussehen zu lassen (braunes Paketdesign mit typischen Verkando Farben & Elementen). Es sollte jedoch kein Verkando Logo oder rechtlich geschützte Elemente enthalten sein.
Auf dem Cover sollen folgende Texte verbaut sein:
Titel : DAS TOPLISTEN WERK
Untertitel: In 99 Etappen zum Toplisten-Hit auf Verkando
Authoren: Jonas Weitbrecht, Lukas Dornfeld, Tobias Quernheim
Webseite: vkd-profis.de
Beschreibung (optional): Eine vollumfängliche Anleitung rund um das Thema 'Verkando VLS'. Von der Unternehmensgründung, über die Produktrecherche bis hin zur Markteinführung deines ersten Produktes.

```html
<!DOCTYPE html>
<html lang="de">
<head>
<meta charset="utf-8">
<title>Das Toplisten Werk – Buchcover</title>
<link rel="stylesheet" href="https://fonts.googleapis.com/css2?family=Bebas+Neue&family=Montserrat:wght@700;800&family=Courier+Prime&display=swap">
<style>
  :root{
    --page:#e8e8e8;
    --cover-dark:#2c3239;
    --cover-mid:#3d4348;
    --cover-light:#565a53;
    --cream:#f6ecd6;
    --gold-deep:#cfa24c;
    --gold-light:#fcdc98;
    --badge-red:#b03330;
    --badge-ring:#c9a15a;
    --box-light:#d99a4a;
    --box-dark:#9a5f24;
    --tag-black:#0c0c0c;
    --tag-text:#e8c88a;
  }
  *{margin:0;padding:0;box-sizing:border-box}
  html,body{width:1200px;height:1200px;overflow:hidden;background:var(--page)}
  .cover{
    position:absolute;left:212px;top:17px;width:776px;height:1164px;
    background:
      radial-gradient(ellipse at 85% 35%, var(--cover-light) 0%, transparent 60%),
      linear-gradient(180deg, var(--cover-mid) 0%, var(--cover-dark) 55%, #2a2f35 100%);
    overflow:hidden;
  }
  .authors{
    position:absolute;top:26px;left:0;width:100%;text-align:center;
    font-family:"Bebas Neue",sans-serif;font-size:35px;letter-spacing:.5px;color:var(--cream);
    white-space:nowrap;
  }
  .authors .sep{display:inline-block;width:2px;height:22px;background:var(--cream);margin:0 6px;vertical-align:2px}
  .gold{
    background:linear-gradient(90deg,var(--gold-deep),var(--gold-light));
    -webkit-background-clip:text;background-clip:text;color:transparent;
    filter:drop-shadow(3px 4px 3px rgba(0,0,0,.45));
  }
  .title-das{
    position:absolute;top:108px;left:0;width:100%;
    display:flex;justify-content:center;align-items:center;gap:32px;
  }
  .title-das .rule{width:112px;height:3px;background:linear-gradient(90deg,var(--gold-deep),var(--gold-light))}
  .title-das .word{font-family:"Montserrat",sans-serif;font-weight:800;font-size:54px;letter-spacing:12px;line-height:1;padding-left:12px}
  .title-main{
    position:absolute;top:176px;left:0;width:100%;text-align:center;
    font-family:"Bebas Neue",sans-serif;font-size:168px;line-height:1;letter-spacing:1px;
  }
  .title-sub{
    position:absolute;top:312px;left:0;width:100%;text-align:center;
    font-family:"Montserrat",sans-serif;font-weight:800;font-size:178px;line-height:1;letter-spacing:-2px;
  }
  .parcel-art{
    position:absolute;left:117px;top:513px;width:541px;height:475px;
    background:linear-gradient(135deg,var(--box-light) 0%,#c27f36 55%,var(--box-dark) 100%);
    border-radius:6px;
    box-shadow:0 30px 40px rgba(0,0,0,.45);
  }
  .url-tag{
    position:absolute;left:296px;top:556px;width:344px;height:40px;
    background:var(--tag-black);transform:rotate(7deg);
    font-family:"Courier Prime",monospace;font-size:27px;color:var(--tag-text);
    display:flex;align-items:center;justify-content:center;letter-spacing:1px;
  }
  .badge{
    position:absolute;left:62px;top:488px;width:226px;height:226px;border-radius:50%;
    background:var(--badge-red);border:3px solid var(--badge-ring);
    box-shadow:0 6px 14px rgba(0,0,0,.4);
    display:flex;align-items:center;justify-content:center;text-align:center;
  }
  .badge p{
    transform:rotate(-12deg);
    font-family:"Bebas Neue",sans-serif;color:var(--cream);font-size:31px;line-height:1.05;
  }
  .badge .num{font-size:44px}
  .description{
    position:absolute;top:1026px;left:0;width:100%;text-align:center;
    font-family:"Bebas Neue",sans-serif;font-size:27px;line-height:35px;letter-spacing:.8px;color:var(--cream);
  }
</style>
</head>
<body>
  <main class="cover">
    <p class="authors">Jonas Weitbrecht<span class="sep"></span>Lukas Dornfeld<span class="sep"></span>Tobias Quernheim</p>

    <h1>
      <span class="title-das"><span class="rule"></span><span class="word gold">DAS</span><span class="rule"></span></span>
      <span class="title-main gold">TOPLISTEN</span>
      <span class="title-sub gold">WERK</span>
    </h1>

    <div class="parcel-art" role="img" aria-label="Illustration eines braunen Versandpakets mit gelbem Klebeband"></div>
    <div class="url-tag">www.vkd-profis.de</div>

    <div class="badge">
      <p>In <span class="num">99</span><br>Etappen zum<br>Toplisten-Hit auf<br>Verkando</p>
    </div>

    <p class="description">
      Eine vollumfängliche Anleitung rund um das Thema ‚Verkando VLS‘.<br>
      Von der Unternehmensgründung, über die Produktrecherche bis<br>
      hin zur Markteinführung deines ersten Produktes.
    </p>
  </main>
</body>
</html>
```